P&H RESTORATION

I want a brochure similiar to the example i've attached.
My company name is P&H Restoration. The website is: P-H-Restoration.com.
The phone number is 803.417.9056.

I don't like the "yellow" being the main color of the example so I'm open to suggestions. I want something CLEAN & Simple, like our logo . This will be a bi fold brochure

```html
<!DOCTYPE html>
<html lang="en">
<head>
<meta charset="utf-8">
<title>P&amp;H Restoration – Bi-fold Brochure</title>
<link href="https://fonts.googleapis.com/css2?family=Montserrat:wght@300;400;600&display=swap" rel="stylesheet">
<style>
:root{
  --cyan:#14bbef;
  --blue:#0b8dcc;
  --navy:#2c3440;
  --band:rgba(38,45,56,.92);
  --ink-soft:#c9ecfa;
  --white:#ffffff;
  --stage:#e8e9eb;
  --photo-warm-a:#d9c7a6;
  --photo-warm-b:#8a5a36;
}
*{box-sizing:border-box;margin:0;padding:0}
html,body{width:1200px;height:838px;overflow:hidden;background:var(--stage);font-family:"Montserrat",sans-serif;color:var(--white)}
.sheet{position:absolute;display:flex}
.sheet--p1{left:37px;top:70px}
.sheet--p2{left:332px;top:70px}
.sheet--p3{left:631px;top:70px}
.sheet--p4{left:926px;top:70px}
.sheet--outside{left:37px;top:454px}
.sheet--inside{left:631px;top:454px}
.panel{position:relative;overflow:hidden;container-type:inline-size;aspect-ratio:460/595;box-shadow:0 6px 14px rgba(0,0,0,.18)}
.sheet--p1 .panel,.sheet--p2 .panel,.sheet--p3 .panel,.sheet--p4 .panel{width:240px}
.sheet--outside .panel,.sheet--inside .panel{width:268px}
.fill{position:absolute;inset:0;width:100%;height:100%}

/* bands */
.mid-band{position:absolute;left:0;right:0;top:61.2%;height:6.9%;background:var(--band);display:flex;align-items:center}

/* brand */
.brand{position:absolute;display:flex;align-items:center;gap:2cqw;font-weight:400;color:var(--white);white-space:nowrap}
.brand__mark{flex:none;width:3.2cqw;height:3.2cqw;border:0.4cqw solid currentColor}

/* cover */
.cover{background:var(--cyan)}
.cover .brand{left:36%;top:46%;font-size:5.2cqw}
.tagline{width:100%;text-align:center;font-size:3.4cqw;letter-spacing:.36em;font-weight:400;padding-left:4%;white-space:nowrap}
.cover__url{position:absolute;left:0;right:0;top:72.5%;text-align:center;font-size:3.3cqw;font-weight:300;padding-left:4%}

/* testimonials */
.reviews{background:var(--cyan)}
.reviews__blueprint{position:absolute;left:0;right:0;top:68.1%;bottom:0;background:linear-gradient(180deg,#13b3e8,#19c1f1)}
.reviews__lead{position:absolute;left:7%;top:4.8%;font-size:3.4cqw;font-weight:400}
.reviews .brand{left:7%;top:11.5%;font-size:5.4cqw}
.review{position:absolute;left:4.5%;right:5.5%;padding:0 0 1.6cqw 2.5%;border-left:1px solid rgba(255,255,255,.75);border-bottom:1px solid rgba(255,255,255,.75);border-bottom-left-radius:2cqw}
.review--1{top:21.8%}
.review--2{top:33.6%}
.review--3{top:47.4%}
.review__name{font-size:3cqw;font-weight:600;line-height:1.2}
.review__text{font-size:2.3cqw;font-weight:300;line-height:1.3}
.contact{width:100%;display:flex;align-items:center;justify-content:space-between;padding:0 3.5% 0 5.5%;font-size:2.45cqw;font-weight:600;white-space:nowrap}
.contact__item{display:flex;align-items:center;gap:1.4cqw}
.contact__item svg{flex:none;width:2cqw;height:2cqw}
.contact__sep{font-weight:300;opacity:.8;margin:0 .6cqw}

/* inside pages */
.inside{background:var(--blue)}
.inside__photo{position:absolute;left:0;right:0;top:0;height:68.1%;background:linear-gradient(120deg,var(--photo-warm-a) 0%,#c9ad84 45%,var(--photo-warm-b) 100%)}
.inside__head{position:absolute;left:0;right:0;top:0;height:16.7%;background:var(--band);padding:4.6% 6% 0}
.inside__title{font-size:4.3cqw;font-weight:600;line-height:1.2;white-space:nowrap}
.inside__sub{font-size:3cqw;font-weight:600;margin-top:2cqw}
.inside__arc{position:absolute;left:0;top:16.7%;width:100%;height:44.5%}
.sectors{width:100%;display:flex;align-items:center;padding-left:6%;font-size:3.5cqw;font-weight:600}
.sectors__sep{width:1px;height:4.6cqw;background:var(--white);margin:0 7cqw 0 7.5cqw}
.steps{position:absolute;left:0;right:0;top:68.1%;bottom:0;background:linear-gradient(180deg,var(--blue),#0a80bd);display:flex;padding:4cqw 3% 0 6%}
.step{flex:1;padding-right:3cqw}
.step + .step{border-left:1px solid rgba(255,255,255,.55);padding-left:4cqw;padding-right:0}
.step__head{font-size:2.7cqw;font-weight:600;margin-bottom:1cqw;white-space:nowrap}
.step__body{font-size:2.4cqw;font-weight:300;line-height:1.6;color:var(--ink-soft);padding-bottom:5cqw}
</style>
</head>
<body>

<!-- ===== single pages, top row ===== -->
<div class="sheet sheet--p1">
  <section class="panel cover">
    <svg class="fill" viewBox="0 0 460 595" preserveAspectRatio="none" role="img" aria-label="Photo of a flooded living room interior">
      <defs><linearGradient id="flood1" x1="0" y1="0" x2="0" y2="1"><stop offset="0" stop-color="#4a5662"/><stop offset=".6" stop-color="#343c49"/><stop offset="1" stop-color="#1f3a52"/></linearGradient></defs>
      <circle cx="421" cy="297" r="379" fill="url(#flood1)"/>
    </svg>
    <div class="brand"><span class="brand__mark"></span>P&amp;H Restoration</div>
    <div class="mid-band"><p class="tagline">Insurance Claim Specialist</p></div>
    <p class="cover__url">www.P-H-Restoration.com</p>
  </section>
</div>

<div class="sheet sheet--p2">
  <section class="panel inside">
    <div class="inside__photo" role="img" aria-label="Photo of a renovated kitchen framed by two hands"></div>
    <svg class="inside__arc" viewBox="0 0 460 264" preserveAspectRatio="none"><path d="M0 0H124Q46 130 59 264H0Z" fill="var(--cyan)"/></svg>
    <header class="inside__head"><h2 class="inside__title">Restoration or Renovation?</h2><p class="inside__sub">What happens after the cleanup?</p></header>
    <div class="mid-band"><div class="sectors">COMMERCIAL<span class="sectors__sep"></span>RESIDENTIAL</div></div>
    <div class="steps">
      <div class="step"><h3 class="step__head">1. Adjuster's Inspection</h3><p class="step__body">Feel Confident. Be sure you received a fair and accurate assessment &amp; repair of all damages with our team's use of industry leading Estimating Systems and On-Site Review.</p></div>
      <div class="step"><h3 class="step__head">2. Timely Settlement</h3><p class="step__body">Don't wait. Minimize the hassle of long processing times from Estimate to Settlement when you team up with an Insurance Claim Specialist.</p></div>
    </div>
  </section>
</div>

<div class="sheet sheet--p3">
  <section class="panel inside">
    <div class="inside__photo" role="img" aria-label="Photo of a renovated kitchen framed by two hands"></div>
    <header class="inside__head"><h2 class="inside__title">Here For You, Every Step Of The Way</h2><p class="inside__sub">www.P-H-Restoration.com</p></header>
    <div class="mid-band"></div>
    <div class="steps">
      <div class="step"><h3 class="step__head">3. Under One Roof</h3><p class="step__body">Don't Worry. You won't need to arrange meetings with multiple contractors; we'll take care of everything from demo to final cleanup.</p></div>
      <div class="step"><h3 class="step__head">4. Superior Craftsmanship</h3><p class="step__body">Don't settle for satisfactory. Our team is committed to the highest standards of excellence every step of the way. Trust us when we say that we'll make you smile.</p></div>
    </div>
  </section>
</div>

<div class="sheet sheet--p4">
  <section class="panel reviews">
    <div class="reviews__blueprint" role="img" aria-label="Faint architectural blueprint drawing"></div>
    <p class="reviews__lead">Specializing in Insurance Claims</p>
    <div class="brand"><span class="brand__mark"></span>P&amp;H Restoration</div>
    <div class="review review--1"><p class="review__name">Daniel K</p><p class="review__text">Owen was so great to work with. He made dealing with my insurance company simple and easy. Highly recommend.</p></div>
    <div class="review review--2"><p class="review__name">Laura S</p><p class="review__text">P&amp;H Restoration was a pleasure to work with. They worked with my insurance company on my behalf to ensure I received a fair settlement and that my home was restored properly after unfortunate water damage.</p></div>
    <div class="review review--3"><p class="review__name">Renee T</p><p class="review__text">Very professional, responsive, and efficient. They repaired my home in just a few weeks</p></div>
    <div class="mid-band"><div class="contact">
      <span class="contact__item"><svg viewBox="0 0 16 12"><rect x="0" y="0" width="16" height="12" rx="1" fill="#fff"/><path d="M1 1l7 6 7-6" fill="none" stroke="#2c3440" stroke-width="1.4"/></svg>www.P-H-Restoration.com</span>
      <span class="contact__item"><svg viewBox="0 0 16 16"><path d="M4 1l3 3-2 2c1 2 3 4 5 5l2-2 3 3-2 2C7 14 2 9 2 3z" fill="#fff"/></svg>803.417.9056<span class="contact__sep">|</span>803.417.9071</span>
    </div></div>
  </section>
</div>

<!-- ===== outside spread ===== -->
<div class="sheet sheet--outside">
  <section class="panel reviews">
    <div class="reviews__blueprint" role="img" aria-label="Faint architectural blueprint drawing"></div>
    <p class="reviews__lead">Specializing in Insurance Claims</p>
    <div class="brand"><span class="brand__mark"></span>P&amp;H Restoration</div>
    <div class="review review--1"><p class="review__name">Daniel K</p><p class="review__text">Owen was so great to work with. He made dealing with my insurance company simple and easy. Highly recommend.</p></div>
    <div class="review review--2"><p class="review__name">Laura S</p><p class="review__text">P&amp;H Restoration was a pleasure to work with. They worked with my insurance company on my behalf to ensure I received a fair settlement and that my home was restored properly after unfortunate water damage.</p></div>
    <div class="review review--3"><p class="review__name">Renee T</p><p class="review__text">Very professional, responsive, and efficient. They repaired my home in just a few weeks</p></div>
    <div class="mid-band"><div class="contact">
      <span class="contact__item"><svg viewBox="0 0 16 12"><rect x="0" y="0" width="16" height="12" rx="1" fill="#fff"/><path d="M1 1l7 6 7-6" fill="none" stroke="#2c3440" stroke-width="1.4"/></svg>www.P-H-Restoration.com</span>
      <span class="contact__item"><svg viewBox="0 0 16 16"><path d="M4 1l3 3-2 2c1 2 3 4 5 5l2-2 3 3-2 2C7 14 2 9 2 3z" fill="#fff"/></svg>803.417.9056<span class="contact__sep">|</span>803.417.9071</span>
    </div></div>
  </section>
  <section class="panel cover">
    <svg class="fill" viewBox="0 0 460 595" preserveAspectRatio="none" role="img" aria-label="Photo of a flooded living room interior">
      <defs><linearGradient id="flood2" x1="0" y1="0" x2="0" y2="1"><stop offset="0" stop-color="#4a5662"/><stop offset=".6" stop-color="#343c49"/><stop offset="1" stop-color="#1f3a52"/></linearGradient></defs>
      <circle cx="421" cy="297" r="379" fill="url(#flood2)"/>
    </svg>
    <div class="brand"><span class="brand__mark"></span>P&amp;H Restoration</div>
    <div class="mid-band"><p class="tagline">Insurance Claim Specialist</p></div>
    <p class="cover__url">www.P-H-Restoration.com</p>
  </section>
</div>

<!-- ===== inside spread ===== -->
<div class="sheet sheet--inside">
  <section class="panel inside">
    <div class="inside__photo" role="img" aria-label="Photo of a renovated kitchen framed by two hands"></div>
    <svg class="inside__arc" viewBox="0 0 460 264" preserveAspectRatio="none"><path d="M0 0H124Q46 130 59 264H0Z" fill="var(--cyan)"/></svg>
    <header class="inside__head"><h2 class="inside__title">Restoration or Renovation?</h2><p class="inside__sub">What happens after the cleanup?</p></header>
    <div class="mid-band"><div class="sectors">COMMERCIAL<span class="sectors__sep"></span>RESIDENTIAL</div></div>
    <div class="steps">
      <div class="step"><h3 class="step__head">1. Adjuster's Inspection</h3><p class="step__body">Feel Confident. Be sure you received a fair and accurate assessment &amp; repair of all damages with our team's use of industry leading Estimating Systems and On-Site Review.</p></div>
      <div class="step"><h3 class="step__head">2. Timely Settlement</h3><p class="step__body">Don't wait. Minimize the hassle of long processing times from Estimate to Settlement when you team up with an Insurance Claim Specialist.</p></div>
    </div>
  </section>
  <section class="panel inside">
    <div class="inside__photo" role="img" aria-label="Photo of a renovated kitchen framed by two hands"></div>
    <header class="inside__head"><h2 class="inside__title">Here For You, Every Step Of The Way</h2><p class="inside__sub">www.P-H-Restoration.com</p></header>
    <div class="mid-band"></div>
    <div class="steps">
      <div class="step"><h3 class="step__head">3. Under One Roof</h3><p class="step__body">Don't Worry. You won't need to arrange meetings with multiple contractors; we'll take care of everything from demo to final cleanup.</p></div>
      <div class="step"><h3 class="step__head">4. Superior Craftsmanship</h3><p class="step__body">Don't settle for satisfactory. Our team is committed to the highest standards of excellence every step of the way. Trust us when we say that we'll make you smile.</p></div>
    </div>
  </section>
</div>

</body>
</html>
```